Need updated stationery design for chiropractic clinic

We recently moved our office and are looking to refresh our letterhead, business cards, presentation folder and envelopes. I tend to prefer simple, clean designs. We communicate with a lot of attorneys and want to exude professionalism. I have attached our logo and 2 additional versions (all white and white letters instead of grey).

Target Market(s)

Other medical professionals and attorneys. Business cards will go to patients as well.

Industry/Entity Type

Healthcare

```html
<!DOCTYPE html>
<html lang="en">
<head>
<meta charset="UTF-8">
<title>SpineWell Injury Care Clinic – Business Card</title>
<link href="https://fonts.googleapis.com/css2?family=Source+Sans+3:wght@400;600;700&display=swap" rel="stylesheet">
<style>
  :root {
    --bg: #e4e4e4;
    --card: #fdfdfd;
    --teal: #2ec3c7;
    --blue: #1a8ed6;
    --brand: #1ea3d6;
    --grey-text: #4a4a4a;
    --dark-text: #333333;
  }
  * { margin: 0; padding: 0; box-sizing: border-box; }
  html, body {
    width: 1200px; height: 800px; overflow: hidden;
    background: var(--bg);
    font-family: "Source Sans 3", "Myriad Pro", sans-serif;
  }
  .canvas {
    position: relative; width: 1200px; height: 800px;
    display: flex; align-items: center; justify-content: center; gap: 40px;
  }
  .card {
    position: relative; width: 520px; height: 297px;
    background: var(--card);
    overflow: hidden;
    box-shadow: 0 6px 18px rgba(0,0,0,0.12);
  }
  .band {
    position: absolute; top: 0; height: 100%;
    background: linear-gradient(165deg, var(--teal) 0%, #19b2d2 45%, var(--blue) 100%);
  }
  /* Front */
  .card-front .band { right: 0; width: 29.5%; }
  .brand-lockup {
    position: absolute; left: 62px; top: 118px;
    display: flex; align-items: center; gap: 12px;
  }
  .brand-mark {
    width: 44px; height: 44px; background: var(--brand); flex-shrink: 0;
  }
  .brand-name {
    font-weight: 700; font-size: 32px; line-height: 1; color: var(--brand);
  }
  .brand-tagline {
    font-weight: 400; font-size: 17px; color: var(--grey-text);
    letter-spacing: 0.2px; margin-top: 3px;
  }
  /* Back */
  .card-back .band { left: 0; width: 31%; }
  .band-brand {
    position: absolute; left: 22px; bottom: 26px; color: #fff;
  }
  .band-brand .name { font-weight: 700; font-size: 22px; line-height: 1; }
  .band-brand .tagline { font-size: 11px; margin-top: 2px; letter-spacing: 0.2px; }
  .person {
    position: absolute; left: 196px; top: 44px;
  }
  .person-name {
    font-weight: 600; font-size: 42px; line-height: 1; color: var(--blue);
  }
  .person-title {
    font-size: 19px; color: var(--teal); margin-top: 4px;
  }
  .contacts {
    position: absolute; left: 196px; top: 165px;
    list-style: none; display: flex; flex-direction: column; gap: 12px;
  }
  .contact {
    display: flex; align-items: center; gap: 12px;
    font-size: 16px; color: var(--dark-text);
  }
  .contact svg { width: 24px; height: 24px; flex-shrink: 0; }
</style>
</head>
<body>
<main class="canvas">
  <section class="card card-front" aria-label="Business card front">
    <div class="brand-lockup">
      <span class="brand-mark" aria-hidden="true"></span>
      <div>
        <div class="brand-name">SpineWell</div>
        <div class="brand-tagline">INJURY CARE CLINIC</div>
      </div>
    </div>
    <div class="band" aria-hidden="true"></div>
  </section>

  <section class="card card-back" aria-label="Business card back">
    <div class="band">
      <div class="band-brand">
        <div class="name">SpineWell</div>
        <div class="tagline">INJURY CARE CLINIC</div>
      </div>
    </div>
    <div class="person">
      <div class="person-name">Your Name</div>
      <div class="person-title">Chiropractic Spealist</div>
    </div>
    <ul class="contacts">
      <li class="contact">
        <svg viewBox="0 0 24 24" aria-hidden="true"><circle cx="12" cy="12" r="12" fill="#1a8ed6"/><path d="M9 6.5l1.6 2.8-1.2 1.2c.7 1.6 2 2.9 3.6 3.6l1.2-1.2 2.8 1.6-.8 2.3c-4.6-.3-8.4-4.1-8.7-8.7z" fill="#fff"/></svg>
        0123-456-78
      </li>
      <li class="contact">
        <svg viewBox="0 0 24 24" aria-hidden="true"><circle cx="12" cy="12" r="12" fill="#1a8ed6"/><rect x="6.5" y="8" width="11" height="8" fill="#fff"/><path d="M6.5 8l5.5 4.5L17.5 8" fill="none" stroke="#1a8ed6" stroke-width="1.2"/></svg>
        yourname@email.com
      </li>
      <li class="contact">
        <svg viewBox="0 0 24 24" aria-hidden="true"><circle cx="12" cy="12" r="12" fill="#1a8ed6"/><path d="M12 5.5a4.3 4.3 0 0 0-4.3 4.3c0 3.2 4.3 8.2 4.3 8.2s4.3-5 4.3-8.2A4.3 4.3 0 0 0 12 5.5z" fill="#fff"/><circle cx="12" cy="9.8" r="1.6" fill="#1a8ed6"/></svg>
        123 Street, State, Poscode
      </li>
    </ul>
  </section>
</main>
</body>
</html>
```